Redesign of the Klammbrot label

I am a pharmacist and sell a bitters called "Klammbrot". I would like to revise and modernize the current logo of my "Klammbrot". I have attached a photo of the current label. I have different bottle sizes with different label sizes, but for now I will only need one label for the 700ml size:
20ml 36x47mm
40ml 45x62mm
200ml 70x91mm
350ml 70x98mm
500ml 70x110mm
700ml 87x119mm
The Uffe is a small stream that runs through our town. The Klammbrot is a play on words that takes up the mysticism of the Harz, as a spirit can of course also be a schnapps. I like the mysticism and rough nature of the Harz in connection with the product. I have attached a logo suggestion that I once had an AI design. But I am very open to new ideas. A connection to my pharmacy does not necessarily have to be recognizable. VG, K. Brandis

Target Market(s)

End consumers, gastronomy, restaurants, hotels

```html
<!DOCTYPE html>
<html lang="de">
<head>
<meta charset="utf-8">
<title>Klammbrot – Etikett 700 ml</title>
<link href="https://fonts.googleapis.com/css2?family=Orbitron:wght@500;700&family=Open+Sans:wght@400&display=swap" rel="stylesheet">
<style>
  :root {
    --label-tan: #e3bd7e;
    --label-brown: #603618;
  }
  html, body {
    margin: 0;
    padding: 0;
    width: 737px;
    height: 1200px;
    overflow: hidden;
    background: var(--label-tan);
  }
  .label { display: block; width: 737px; height: 1200px; }
  .display { font-family: "Orbitron", sans-serif; font-weight: 700; fill: var(--label-tan); }
  .claim { font-family: "Orbitron", sans-serif; font-weight: 500; fill: var(--label-tan); }
  .body-text { font-family: "Open Sans", sans-serif; font-weight: 400; fill: var(--label-tan); }
  .band-text { font-family: "Open Sans", sans-serif; fill: var(--label-brown); }
  .pill-text { font-family: "Orbitron", sans-serif; font-weight: 700; fill: var(--label-brown); }
  .frame { fill: none; stroke: var(--label-tan); stroke-width: 2; }
</style>
</head>
<body>
<svg class="label" viewBox="0 0 737 1200" xmlns="http://www.w3.org/2000/svg" role="img" aria-label="Klammbrot Bitterlikör Etikett">
  <!-- background panels -->
  <rect class="panel-main" x="23" y="20" width="683" height="964" fill="var(--label-brown)"/>
  <rect class="panel-foot" x="23" y="1016" width="683" height="164" fill="var(--label-brown)"/>

  <!-- inner frame -->
  <rect class="frame" x="51" y="63" width="629" height="1095" rx="34"/>
  <rect class="info-band" x="23" y="984" width="683" height="32" fill="var(--label-tan)"/>

  <!-- header -->
  <text class="display" x="374" y="181" text-anchor="middle" font-size="33" textLength="307" lengthAdjust="spacingAndGlyphs">BAD TANNRODER</text>
  <text class="display" x="355" y="219" text-anchor="middle" font-size="19" textLength="145" lengthAdjust="spacingAndGlyphs">ERLESENER</text>
  <text class="display product-name" x="362" y="324" text-anchor="middle" font-size="84" textLength="500" lengthAdjust="spacingAndGlyphs">KLAMMBROT</text>

  <!-- description box -->
  <rect class="frame" x="82" y="378" width="566" height="269" rx="22"/>
  <rect class="pill" x="271" y="360" width="199" height="31" rx="15.5" fill="var(--label-tan)"/>
  <text class="pill-text" x="370" y="383" text-anchor="middle" font-size="19" textLength="142" lengthAdjust="spacingAndGlyphs">BITTERLIKÖR</text>

  <g class="claim" font-size="17">
    <text x="365" y="417" text-anchor="middle" font-size="20" textLength="366" lengthAdjust="spacingAndGlyphs">NACH ALTER APOTHEKERKUNST</text>
    <text x="365" y="452" text-anchor="middle" textLength="539" lengthAdjust="spacingAndGlyphs">EINE ZUBEREITUNG NACH HÖCHST GEHEIMEM REZEPT.</text>
    <text x="365" y="487" text-anchor="middle" textLength="397" lengthAdjust="spacingAndGlyphs">SIE SEI EMPFOHLEN ZUM GENUSS NACH</text>
    <text x="369" y="522" text-anchor="middle" textLength="203" lengthAdjust="spacingAndGlyphs">EINEM GUTEN MAHL.</text>
    <text x="362" y="556" text-anchor="middle" textLength="541" lengthAdjust="spacingAndGlyphs">AUFS FEINSTE ZUBEREITET MIT GEISTIGEN AUSZÜGEN</text>
    <text x="362" y="592" text-anchor="middle" textLength="440" lengthAdjust="spacingAndGlyphs">VON ENZIAN, KALMUS, MALABAR-KARDAMOM</text>
    <text x="365" y="627" text-anchor="middle" textLength="378" lengthAdjust="spacingAndGlyphs">UND ANDEREN WERTVOLLEN ZUTATEN.</text>
  </g>

  <!-- maker block -->
  <text class="body-text" x="153" y="703" font-size="22">Aus der</text>
  <text class="body-text" x="492" y="710" text-anchor="middle" font-size="36" textLength="233" lengthAdjust="spacingAndGlyphs">700ml 34% vol</text>

  <g class="display" font-size="29" text-anchor="middle">
    <text x="216" y="750" textLength="185" lengthAdjust="spacingAndGlyphs">LINDEN</text>
    <text x="216" y="789" textLength="170" lengthAdjust="spacingAndGlyphs">APOTHEKE</text>
    <text x="216" y="829" textLength="205" lengthAdjust="spacingAndGlyphs">BAD TANNRODE</text>
  </g>

  <g class="body-text" font-size="20">
    <text x="132" y="867">Dr. K. Brandis</text>
    <text x="132" y="895">Mühlenweg 12</text>
    <text x="132" y="923">37990 Bad Tannrode</text>
    <text x="132" y="951">Tel.: 05500-1234</text>
  </g>

  <!-- brand mark -->
  <g class="brand-mark">
    <circle cx="509" cy="810" r="22" fill="none" stroke="var(--label-tan)" stroke-width="3"/>
    <text class="display" x="509" y="868" text-anchor="middle" font-size="28">KLAMMBROT</text>
  </g>

  <!-- legal band -->
  <text class="band-text" x="358" y="1006" text-anchor="middle" font-size="15">Kräuterlikör, Chininhaltig L2313886</text>
</svg>
</body>
</html>
```